Pellmore Dental Children's postcard before camp starts

Families are starting to prep their children to go to camp. Sometimes parents forget to have a dental check up during the year and we always have emergencies coming into the office during the summer time.

Pellmore Dental is looking to create a Mailing Postcard to send our community targeting Parents (specifically mothers) to remind them that having a dental check up for their children before camp starts is very important.

We would like to send out the cards to our entire community (over 2000 homes) and so we are looking for a creative design that will have the parents calling us to schedule an appointment for their children before the camp season starts.

We have included a few post cards that we found online that resemble what we are looking for

Its the end of the school year and the start of the summer season so we are looking for a nice summer look and feel.

Younger children need check up and cleanings, teens who play sports should wear sports guards etc.

Target Market(s)

We are targeting mothers/parents with children ages 2-13 in our community

Industry/Entity Type

Dental

Font styles to use
Other font styles liked:
• I do not have a fond in mind but something for children.

Requirements
Must have
• We must have our office information (ie: Logo, telephone number, address). we would love to have children smiling on the cards. We would love to have something look like the "Sprig" pediatric dental.
Nice to have
• front and back side with nice art work,
Should not have
• this is a target for children. Please keep it friendly and fresh looking.

```html
<!DOCTYPE html>
<html lang="en">
<head>
<meta charset="utf-8">
<title>Pellmore Dental – Children's Postcard</title>
<link href="https://fonts.googleapis.com/css2?family=Open+Sans:wght@400;600&family=Gochi+Hand&display=swap" rel="stylesheet">
<style>
  :root {
    --page: #e9e9e9;
    --card: #ffffff;
    --blue: #2a86e6;
    --blue-deep: #1f74d0;
    --brand: #1c72c4;
    --orange: #f7931e;
    --yellow: #fff200;
    --ink: #444444;
    --rule: #cfcfcf;
  }
  * { box-sizing: border-box; margin: 0; padding: 0; }
  html, body { width: 1200px; height: 750px; overflow: hidden; background: var(--page); }
  body { position: relative; font-family: "Open Sans", Arial, sans-serif; }

  .postcard {
    position: absolute;
    top: 180px;
    width: 540px;
    height: 390px;
    background: var(--card);
    overflow: hidden;
    box-shadow: 0 2px 8px rgba(0,0,0,0.12);
  }
  .postcard--front { left: 40px; }
  .postcard--back { left: 620px; }

  /* Front */
  .brand {
    position: absolute;
    top: 30px;
    left: 0;
    width: 100%;
    display: flex;
    justify-content: center;
    align-items: center;
    gap: 12px;
  }
  .brand__mark {
    width: 42px; height: 42px;
    border-radius: 50%;
    background: var(--brand);
  }
  .brand__name {
    font-family: "Open Sans", Arial, sans-serif;
    font-weight: 600;
    font-size: 30px;
    letter-spacing: 1px;
    color: var(--brand);
    line-height: 1;
  }
  .kids-photo {
    position: absolute;
    top: 100px;
    left: 40px;
    width: 460px;
    height: 200px;
    background:
      radial-gradient(ellipse at 20% 55%, #b07a55 0%, rgba(176,122,85,0) 45%),
      radial-gradient(ellipse at 45% 55%, #d9a882 0%, rgba(217,168,130,0) 40%),
      radial-gradient(ellipse at 65% 50%, #7a4a2e 0%, rgba(122,74,46,0) 42%),
      radial-gradient(ellipse at 85% 45%, #e6c29a 0%, rgba(230,194,154,0) 40%),
      linear-gradient(180deg, #ffffff 0%, #efe6dc 60%, #d8c7b5 100%);
  }
  .front-wave { position: absolute; inset: 0; }
  .headline {
    position: absolute;
    left: 30px;
    right: 30px;
    top: 312px;
    font-family: "Gochi Hand", "Comic Sans MS", cursive;
    font-size: 31px;
    color: var(--yellow);
    text-align: center;
    line-height: 1.1;
  }

  /* Back */
  .back-panel {
    position: absolute;
    top: 0; left: 0;
    width: 250px; height: 100%;
    background: var(--blue);
    padding: 28px 22px 0 24px;
    color: #ffffff;
  }
  .services { list-style: none; font-size: 15px; line-height: 1.35; }
  .cta {
    margin-top: 16px;
    font-family: "Gochi Hand", "Comic Sans MS", cursive;
    font-size: 18px;
    line-height: 1.1;
    color: var(--yellow);
  }
  .contact {
    margin-top: 26px;
    font-size: 8.5px;
    line-height: 1.45;
  }
  .contact__gap { margin-top: 4px; }
  .social {
    position: absolute;
    left: 18px;
    top: 312px;
    width: 150px;
    height: 30px;
    border-radius: 15px;
    background: #ffffff;
    display: flex;
    align-items: center;
    gap: 6px;
    padding-left: 14px;
  }
  .social__dot { width: 18px; height: 18px; border-radius: 50%; background: var(--brand); }
  .web {
    position: absolute;
    left: 34px;
    top: 356px;
    font-size: 8px;
    letter-spacing: 2px;
  }
  .stamp {
    position: absolute;
    top: 26px;
    right: 40px;
    width: 58px;
    height: 58px;
    border: 1px solid var(--rule);
  }
  .to-label {
    position: absolute;
    top: 124px;
    left: 282px;
    font-size: 9px;
    color: var(--ink);
  }
  .address-lines { position: absolute; top: 150px; left: 310px; width: 200px; }
  .address-lines span {
    display: block;
    height: 34px;
    border-bottom: 1px solid var(--rule);
  }
</style>
</head>
<body>

<section class="postcard postcard--front">
  <div class="kids-photo" role="img" aria-label="Photo of four smiling children lying on their fronts, chins resting on their hands"></div>
  <svg class="front-wave" width="540" height="390" viewBox="0 0 540 390" aria-hidden="true">
    <path d="M0,272 Q250,350 540,172 L540,390 L0,390 Z" fill="var(--blue)"/>
    <path d="M0,262 Q250,342 540,162" fill="none" stroke="#ffffff" stroke-width="5"/>
    <path d="M8,254 Q250,336 536,150" fill="none" stroke="var(--orange)" stroke-width="6" stroke-linecap="round"/>
  </svg>
  <div class="brand">
    <span class="brand__mark"></span>
    <span class="brand__name">PELLMORE DENTAL</span>
  </div>
  <p class="headline">Your Child's smile is important to us</p>
</section>

<section class="postcard postcard--back">
  <div class="back-panel">
    <ul class="services">
      <li>Pediatric Dentistry</li>
      <li>Preventive dentistry</li>
      <li>Cosmetic Dentistry</li>
    </ul>
    <p class="cta">Call today to reserve your child's appointment with Dr Nora Lindqvist</p>
    <div class="contact">
      <p>214 Marigold Way</p>
      <p>Fairhaven, Oregon 97120</p>
      <p class="contact__gap">555 210 4417</p>
      <p>555 318 2290</p>
      <p>555 764 0182</p>
      <p>hello@pellmoredental.com</p>
    </div>
    <div class="social">
      <span class="social__dot"></span>
      <span class="social__dot"></span>
      <span class="social__dot"></span>
      <span class="social__dot"></span>
      <span class="social__dot"></span>
    </div>
    <p class="web">www.pellmoredental.com</p>
  </div>
  <div class="stamp"></div>
  <p class="to-label">To</p>
  <div class="address-lines">
    <span></span><span></span><span></span><span></span>
  </div>
</section>

</body>
</html>
```